Mexican Restaurant needs a new Menu Design

Mexican restaurant LA TORTUGA VERDE is renewing its menu, so we need something new.
Since our inception we have given the task of rescuing ingredients, recipes, and traditional and representatives dishes of the culinary techniques of yesteryear.
We are the only restaurant in Guadalajara that manufactures its own dairy natural as fresh cheese, the cream and our already well-known and traditional jocoqui. In addition, we produce organic ranch egg and are currently in the development of organic vegetables cultivated on the slopes of the old Hill which gives our plants benefit from an exceptional microclimate.
Find more information about the restaurant in www.latortugaverde.com.
The menu needs to have the full list of products with the prices, some phrases that speak of the philosophy of the ranch-style-living, photos.
We need the cover, back cover and interiors.
Updates
Thank you so much for the proposals you have submitted for the menu design. We are looking them carefully.
Thank you very much for taking your time to design a proposal for our menu!!!
Target Market(s)
The target is very wide (28-40 yrs.): Young executives, Young families, Housewives.
Industry/Entity Type
Restaurant
Look and feel
Each slider illustrates characteristics of the customer's brand and the style your logo design should communicate.

```html
<!DOCTYPE html>
<html lang="es">
<head>
<meta charset="utf-8">
<title>La Tortuga Verde — Menu Cover</title>
<link rel="stylesheet" href="https://fonts.googleapis.com/css2?family=Quattrocento:wght@400;700&display=swap">
<style>
  :root {
    --cover-slate: #3a3a3c;
    --grommet-cream: #fdf6dc;
    --grommet-hole: #000000;
    --cord-red: #d9452f;
    --cord-shade: #b8392a;
    --title-white: #ffffff;
  }
  html, body {
    margin: 0;
    padding: 0;
    overflow: hidden;
  }
  .menu-cover {
    position: relative;
    width: 1200px;
    height: 1000px;
    background: var(--cover-slate);
    overflow: hidden;
  }
  .binding {
    position: absolute;
    left: 0;
    top: 0;
  }
  .restaurant-name {
    position: absolute;
    right: 70px;
    bottom: 38px;
    margin: 0;
    text-align: right;
    color: var(--title-white);
    font-family: "Quattrocento", Georgia, serif;
  }
  .restaurant-name__title {
    display: block;
    font-weight: 400;
    font-size: 68px;
    line-height: 1;
    font-variant: small-caps;
    letter-spacing: 1px;
  }
  .restaurant-name__subtitle {
    display: block;
    margin-top: 4px;
    font-weight: 700;
    font-size: 30px;
    line-height: 1.1;
  }
</style>
</head>
<body>
  <main class="menu-cover">
    <svg class="binding" width="140" height="1000" viewBox="0 0 140 1000" aria-hidden="true">
      <circle class="grommet-ring" cx="77" cy="195" r="24" fill="var(--grommet-cream)"/>
      <circle class="grommet-hole" cx="77" cy="195" r="17" fill="var(--grommet-hole)"/>
      <circle class="grommet-ring" cx="77" cy="806" r="24" fill="var(--grommet-cream)"/>
      <circle class="grommet-hole" cx="77" cy="806" r="17" fill="var(--grommet-hole)"/>
      <rect class="cord" x="72" y="195" width="11" height="611" fill="var(--cord-red)"/>
      <rect class="cord-edge" x="81" y="195" width="2" height="611" fill="var(--cord-shade)"/>
      <rect class="cord-end" x="72" y="193" width="11" height="10" fill="#2a1a17"/>
      <rect class="cord-end" x="72" y="798" width="11" height="10" fill="#2a1a17"/>
    </svg>

    <h1 class="restaurant-name">
      <span class="restaurant-name__title">La Tortuga Verde</span>
      <span class="restaurant-name__subtitle">Restaurante</span>
    </h1>
  </main>
</body>
</html>
```